VORTEK Studio Shape your ideas

VORTEK Studio is a soci% 26 # 233; t% 26 # 233; of mobile application design and multiexperience destiny% 26 # 233; % 26 # 224; The% 26 # 39; industry and particularly the watch industry% 26 # 232; re. By multiexperience, I mean applications usable on watches,% 26 # 233; holographic screens,% 26 # 233; touch screens g% 26 # 233; ant, r% 26 # 233; alit% 26 # 233; virtual,% 26 # 224; distance with a gripsense and% 26 # 233; obviously on mobile on tablet and smartphone. Applications will call% 26 # 224; 3d, artificial intelligence, big data. The company logo% 26 # 233; t% 26 # 233; is attached% 26 # 233; below.

Target Market(s)

Swiss precision industry Watchmaking industry% 26 # 232; re

Coding

Coded - Design and coding required

Font styles to use
Sans Serif

Colors

Designer to choose colors to be used in the design.

Requirements
Must have
• A Contact form A gallery of Vid% 26 # 233; o / Photo (portfolio) 3D images of% 26 # 39; illustration orient% 26 # 233; es industry but% 26 # 233; also luxury (take free images A partner page
Nice to have
• A blog
Should not have
• The designs are too loaded, the page should load quickly.

```html
<!DOCTYPE html>
<html lang="en">
<head>
<meta charset="utf-8">
<title>VORTEK Studio</title>
<link href="https://fonts.googleapis.com/css2?family=Poppins:wght@400;500;600;700;800&family=Rubik:wght@300;400;500&display=swap" rel="stylesheet">
<style>
:root{
  --blue:#0b6ec4;
  --ink:#1e1e1e;
  --text:#7a7a7a;
  --muted:#a3a3a3;
  --line:#e4e4e4;
  --soft:#f7f7f7;
  --footer:#222222;
  --white:#ffffff;
}
*{margin:0;padding:0;box-sizing:border-box}
html,body{width:1200px;height:4996px;overflow:hidden;background:var(--white)}
body{position:relative;font-family:"Rubik",sans-serif;color:var(--ink)}
.abs{position:absolute}
.brand{font-family:"Poppins",sans-serif;font-weight:600;color:var(--blue);font-size:26px;letter-spacing:2px;display:flex;align-items:center;gap:10px}
.brand .dot{width:12px;height:12px;background:var(--blue)}
.topbar{top:22px;right:127px;display:flex;align-items:center;gap:22px;font-size:12px;color:var(--muted)}
.topbar span{display:flex;align-items:center;gap:8px}
.socials{display:flex;gap:6px}
.socials i{width:20px;height:20px;border:1px solid #9a9a9a;border-radius:50%;display:block}
.nav{top:62px;right:127px;display:flex;gap:50px;font-family:"Poppins",sans-serif;font-size:12px;color:#444}
.nav .active{color:var(--blue)}
.hero{top:97px;left:0;width:1200px;height:609px;background:linear-gradient(110deg,#dfe8f5 0%,#9ab6e3 30%,#3d6fc9 60%,#1c47a6 100%)}
.hero h1{position:absolute;left:126px;top:182px;font-family:"Poppins",sans-serif;font-weight:800;font-size:46px;line-height:66px;color:#111;letter-spacing:1px}
.hero p{position:absolute;left:126px;top:322px;font-size:15px;font-weight:500;color:#111}
.btn{background:var(--blue);color:var(--white);font-family:"Poppins",sans-serif;font-weight:600;font-size:11px;letter-spacing:.5px;border-radius:23px;display:flex;align-items:center;justify-content:center;gap:8px}
.label{font-family:"Poppins",sans-serif;font-weight:700;font-size:12.5px;letter-spacing:2px;color:#222;display:flex;align-items:center;gap:16px}
.label::after{content:"";width:80px;height:2px;background:#333}
.h2{font-family:"Poppins",sans-serif;font-weight:700;font-size:34px;line-height:45px;color:#222}
.h2 em{font-style:normal;color:var(--blue)}
.para{font-size:12.5px;line-height:24px;color:var(--text)}
.photo{background:linear-gradient(135deg,#c9d8ec,#6f95c8)}
.center-label{font-family:"Poppins",sans-serif;font-weight:700;font-size:12.5px;letter-spacing:2px;text-align:center}
.features{top:2101px;left:0;width:1200px;height:629px;background:var(--soft)}
.feat{position:absolute;left:597px;display:flex;gap:20px}
.feat h4{font-family:"Poppins",sans-serif;font-weight:400;font-size:19px;color:#222;margin-bottom:6px}
.feat p{font-size:11.5px;line-height:20px;color:var(--text);width:280px}
.card{top:2819px;left:126px;width:947px;height:227px;background:var(--white);box-shadow:0 2px 14px rgba(0,0,0,.09)}
.faq{left:607px;width:466px;height:46px;background:var(--white);box-shadow:0 2px 10px rgba(0,0,0,.08);display:flex;align-items:center;justify-content:space-between;padding:0 20px;font-family:"Poppins",sans-serif;font-size:12px;color:#333}
.faq b{width:16px;height:16px;border:1px solid #bbb;border-radius:50%;display:flex;align-items:center;justify-content:center;font-weight:400;font-size:12px;color:#666}
.faq.open{background:var(--blue);color:var(--white);font-weight:600}
.faq.open b{background:var(--white);color:var(--blue);border-color:var(--white)}
.news{top:3473px;left:0;width:1200px;height:494px;background:var(--soft)}
.field{position:absolute;font-size:11px;color:var(--muted);border-bottom:1px solid var(--line);height:30px}
.footer{top:4590px;left:0;width:1200px;height:406px;background:var(--footer)}
.footer h5{font-family:"Poppins",sans-serif;font-weight:600;font-size:14px;letter-spacing:2px;color:var(--white)}
.footer ul{list-style:none;font-size:12px;color:#c8c8c8;line-height:29px}
.info{display:flex;gap:22px;align-items:flex-start;font-size:13px;color:#444;line-height:22px}
</style>
</head>
<body>

<!-- header -->
<div class="abs brand" style="left:126px;top:30px"><span class="dot"></span>VORTEK</div>
<div class="abs topbar">
  <span><svg width="14" height="14" viewBox="0 0 24 24"><path fill="#0b6ec4" d="M6.6 10.8a15 15 0 006.6 6.6l2.2-2.2a1 1 0 011-.25 11.4 11.4 0 003.6.57 1 1 0 011 1V20a1 1 0 01-1 1A17 17 0 013 4a1 1 0 011-1h3.5a1 1 0 011 1c0 1.25.2 2.45.57 3.57a1 1 0 01-.25 1z"/></svg>Call : (555) 014 2290</span>
  <span><svg width="14" height="10" viewBox="0 0 14 10"><rect width="14" height="10" rx="1" fill="#0b6ec4"/><path d="M1 1l6 4 6-4" stroke="#fff" fill="none"/></svg>hello@vortekmail.net</span>
  <span class="socials"><i></i><i></i><i></i><i></i></span>
</div>
<nav class="abs nav"><span class="active">HOME</span><span>ABOUT US</span><span>PARTNERS</span><span>PORTFOLIO</span><span>CONTACT US</span></nav>

<!-- hero -->
<section class="abs hero" role="img" aria-label="Luxury watch face glowing with a holographic app interface">
  <h1>INNOVATION FOR A<br>BETTER TOMORROW</h1>
  <p>Apps for watches, holograms and every precision screen</p>
  <div class="btn" style="position:absolute;left:126px;top:366px;width:146px;height:43px">CONTACT US</div>
</section>

<!-- about -->
<div class="abs label" style="left:126px;top:832px">ABOUT VORTEK STUDIO</div>
<h2 class="abs h2" style="left:126px;top:880px">We Are <em>Leader</em> in<br>Watch Apps</h2>
<p class="abs para" style="left:126px;top:995px;width:500px">We design mobile and multiexperience applications for the Swiss precision and watchmaking industry. Our interfaces run on watches, holographic screens, giant touch walls and virtual reality, as well as on tablets and smartphones.</p>
<p class="abs para" style="left:126px;top:1092px;width:500px">Each project blends 3D, artificial intelligence and big data with the care of a master watchmaker. From the first sketch to the final release, we keep every screen light, fast and elegant, so your brand feels as refined in the hand as it does on the wrist. Gesture control with gripsense lets clients explore from a distance.</p>
<p class="abs" style="left:126px;top:1234px;width:380px;font-size:14.5px;font-weight:500;line-height:25px">Call us at <span style="color:var(--blue);font-weight:400">555.014.2291</span> or click here to schedule a free consultation.</p>
<div class="abs photo" style="left:692px;top:836px;width:379px;height:446px" role="img" aria-label="Designer testing a smartwatch app in the studio"></div>
<svg class="abs" style="left:726px;top:1176px" width="60" height="60" viewBox="0 0 60 60"><circle cx="30" cy="30" r="29" fill="#fff" opacity=".4"/><circle cx="30" cy="30" r="22" fill="#0b6ec4"/><path d="M26 22l10 8-10 8z" fill="#fff"/></svg>
<div class="abs" style="left:806px;top:1196px;font-family:Poppins,sans-serif;font-weight:600;font-size:12px;letter-spacing:1px;color:#fff">WATCH VIDEO</div>
<div class="abs" style="left:880px;top:1204px;width:150px;height:1px;background:#fff"></div>

<!-- portfolio -->
<div class="abs center-label" style="left:0;top:1433px;width:1200px">OUR PORTFOLIO</div>
<div class="abs" style="left:560px;top:1471px;width:80px;height:2px;background:#333"></div>
<div class="abs photo" style="left:126px;top:1536px;width:299px;height:348px" role="img" aria-label="3D render of a watch movement with app overlay"></div>
<div class="abs photo" style="left:450px;top:1536px;width:299px;height:348px;background:linear-gradient(135deg,#eef1f4,#8fa5b8)" role="img" aria-label="Watchmaker inspecting a dial with a tablet app"></div>
<div class="abs photo" style="left:774px;top:1536px;width:299px;height:348px;background:linear-gradient(135deg,#a9c8ea,#2f68b0)" role="img" aria-label="Holographic display of a luxury timepiece"></div>
<div class="abs btn" style="left:499px;top:1960px;width:201px;height:46px">VIEW ALL PORTFOLIO</div>

<!-- features -->
<section class="abs features">
  <div class="abs photo" style="left:0;top:0;width:506px;height:629px;background:linear-gradient(135deg,#f1f3f5,#9fb7cf)" role="img" aria-label="Hand touching a smartwatch screen"></div>
  <div class="abs label" style="left:601px;top:93px">FEATURES</div>
  <h2 class="abs h2" style="left:601px;top:135px">Why <em>Choose</em> VORTEK<br>Studio Apps?</h2>
  <div class="feat" style="top:264px"><svg width="46" height="46" viewBox="0 0 46 46" fill="none" stroke="#0b6ec4" stroke-width="2"><circle cx="23" cy="23" r="18"/><path d="M15 22h5v10h-5zM20 22l4-7c2 0 3 1 3 3l-1 4h5c2 0 2 2 2 3l-2 6c-1 1-1 1-2 1h-9"/></svg><div><h4>Quality</h4><p>Swiss-grade precision in every pixel, from watch dials to virtual reality.</p></div></div>
  <div class="feat" style="top:360px"><svg width="46" height="46" viewBox="0 0 46 46" fill="none" stroke="#0b6ec4" stroke-width="2"><path d="M17 8h12l-3 6h-6z"/><path d="M20 14c-8 4-11 10-11 16 0 5 4 8 14 8s14-3 14-8c0-6-3-12-11-16"/><text x="23" y="32" font-size="12" fill="#0b6ec4" stroke="none" text-anchor="middle" font-family="Poppins,sans-serif">$</text></svg><div><h4>Great Price</h4><p>One design serves every screen, keeping costs low for our partners.</p></div></div>
  <div class="feat" style="top:458px"><svg width="46" height="46" viewBox="0 0 46 46" fill="none" stroke="#0b6ec4" stroke-width="2"><rect x="12" y="20" width="22" height="18" rx="2"/><path d="M16 20v-5a7 7 0 0114 0v5"/><circle cx="23" cy="28" r="2"/><path d="M23 30v3"/></svg><div><h4>Secure</h4><p>Encrypted data and private AI models protect your brand and clients.</p></div></div>
</section>

<!-- testimonial -->
<div class="abs card">
  <div class="abs" style="left:52px;top:45px;width:66px;height:66px;border-radius:50%;background:linear-gradient(135deg,#e3cfc4,#8a6a5d)" role="img" aria-label="Partner portrait"></div>
  <svg class="abs" style="left:64px;top:162px" width="44" height="10"><circle cx="5" cy="5" r="4" fill="#0b6ec4"/><circle cx="22" cy="5" r="3.5" fill="none" stroke="#bbb"/><circle cx="39" cy="5" r="3.5" fill="none" stroke="#bbb"/></svg>
  <div class="abs" style="left:166px;top:20px;width:1px;height:190px;background:var(--line)"></div>
  <div class="abs" style="left:215px;top:48px;font-family:Poppins,sans-serif;font-weight:500;font-size:14.5px">Oh, my gosh! These guys are awesome.</div>
  <p class="abs para" style="left:215px;top:84px;width:540px">Our new watch app feels as precise as our movements. VORTEK Studio has been a trusted partner from the first sketch to launch day.</p>
  <div class="abs" style="left:215px;top:152px;font-family:Poppins,sans-serif;font-weight:500;font-size:14px;letter-spacing:1.5px;color:var(--blue)">MARC LAVIER</div>
  <div class="abs" style="left:215px;top:174px;font-size:11px;color:var(--muted)">Partner, Watch Manufacture</div>
  <div class="abs" style="left:858px;top:20px;font-family:Poppins,sans-serif;font-weight:800;font-size:80px;color:#e8e8e8">”</div>
</div>

<!-- faq -->
<div class="abs label" style="left:126px;top:3133px">FAQs</div>
<h2 class="abs h2" style="left:126px;top:3178px">We <em>respond</em> to all inquiries<br>received</h2>
<div class="abs btn" style="left:126px;top:3313px;width:196px;height:43px">SEND FOR REQUEST</div>
<div class="abs faq" style="top:3133px">Which devices do your apps run on?<b>+</b></div>
<div class="abs faq open" style="top:3196px">How do we become a VORTEK Studio partner?<b>+</b></div>
<div class="abs faq" style="top:3256px">What is the cost of a watch app?<b>+</b></div>
<div class="abs faq" style="top:3314px">How long does a 3D project take?<b>+</b></div>

<!-- news -->
<section class="abs news">
  <div class="abs label" style="left:126px;top:89px">NEWS</div>
  <h2 class="abs h2" style="left:126px;top:135px">Latest <em>Blog</em> &amp; Post</h2>
  <div class="abs" style="left:126px;top:212px;font-size:11px;color:#555;display:flex;gap:10px;align-items:center"><svg width="12" height="12"><rect x=".5" y="1.5" width="11" height="10" fill="none" stroke="#0b6ec4"/><path d="M0 4h12" stroke="#0b6ec4"/></svg>25 JAN 2020</div>
  <div class="abs" style="left:126px;top:252px;width:400px;font-size:17px;line-height:31px;color:#222">Thoughts On Designing Watch Apps For A Holographic Future</div>
  <p class="abs para" style="left:126px;top:322px;width:430px">How 3D, artificial intelligence and big data are changing the way luxury watch brands talk to their clients on every screen, from wrist to wall.</p>
  <div class="abs" style="left:126px;top:425px;font-family:Poppins,sans-serif;font-weight:700;font-size:64px;color:#ececec;line-height:64px">01</div>
  <div class="abs photo" style="left:749px;top:0;width:451px;height:494px;background:linear-gradient(135deg,#d3dde8,#3f5f86)" role="img" aria-label="Designer pointing at a watch interface on a large screen"></div>
  <div class="abs" style="left:681px;top:436px;width:68px;height:58px;background:#2a2a2a;display:flex;align-items:center;justify-content:center"><svg width="20" height="10"><path d="M20 5H2M6 1L2 5l4 4" stroke="#fff" fill="none" stroke-width="1.5"/></svg></div>
  <div class="abs" style="left:749px;top:436px;width:68px;height:58px;background:var(--blue);display:flex;align-items:center;justify-content:center"><svg width="20" height="10"><path d="M0 5h18M14 1l4 4-4 4" stroke="#fff" fill="none" stroke-width="1.5"/></svg></div>
</section>

<!-- contact -->
<div class="abs label" style="left:126px;top:4115px">CONTACT US</div>
<h2 class="abs h2" style="left:126px;top:4166px;line-height:53px">We're <em>always</em><br>ready to discuss<br>coperation</h2>
<div class="abs info" style="left:126px;top:4352px"><svg width="14" height="18" viewBox="0 0 14 18"><path d="M7 0a7 7 0 017 7c0 5-7 11-7 11S0 12 0 7a7 7 0 017-7z" fill="#0b6ec4"/><circle cx="7" cy="7" r="2.5" fill="#fff"/></svg><span>48 Rue des Horlogers, Ste 12<br>Vallorbe, VD 1337</span></div>
<div class="abs info" style="left:126px;top:4412px"><svg width="14" height="14" viewBox="0 0 24 24"><path fill="#0b6ec4" d="M6.6 10.8a15 15 0 006.6 6.6l2.2-2.2a1 1 0 011-.25 11.4 11.4 0 003.6.57 1 1 0 011 1V20a1 1 0 01-1 1A17 17 0 013 4a1 1 0 011-1h3.5a1 1 0 011 1c0 1.25.2 2.45.57 3.57a1 1 0 01-.25 1z"/></svg><span style="font-weight:500;letter-spacing:1px">555.014.2292</span></div>
<div class="abs info" style="left:126px;top:4455px"><svg width="14" height="10" viewBox="0 0 14 10" style="margin-top:6px"><rect width="14" height="10" rx="1" fill="#0b6ec4"/><path d="M1 1l6 4 6-4" stroke="#fff" fill="none"/></svg><span style="color:var(--blue)">studio@vortekmail.net</span></div>

<div class="abs" style="left:584px;top:4114px;font-size:19px;font-weight:300;color:#333">I would like to discuss:</div>
<div class="field" style="left:584px;top:4180px;width:231px">Name*</div>
<div class="field" style="left:846px;top:4180px;width:227px">Last Name*</div>
<div class="field" style="left:584px;top:4232px;width:231px">Phone*</div>
<div class="field" style="left:846px;top:4232px;width:227px">Email*</div>
<div class="field" style="left:584px;top:4284px;width:489px;display:flex;justify-content:space-between">Are You A Partner<span>▾</span></div>
<div class="field" style="left:584px;top:4340px;width:489px;height:70px">Message</div>
<div class="abs btn" style="left:582px;top:4432px;width:180px;height:43px;font-size:12px;letter-spacing:1.5px">SEND MESSAGE <span>›</span></div>

<!-- footer -->
<footer class="abs footer">
  <div class="abs brand" style="left:126px;top:140px;color:var(--white);font-size:34px"><span class="dot" style="background:var(--white)"></span>VORTEK</div>
  <h5 class="abs" style="left:427px;top:88px">QUICK LINKS</h5>
  <ul class="abs" style="left:427px;top:124px"><li>Home</li><li>About Us</li><li>Portfolio</li><li>Partners</li><li>Contact Us</li></ul>
  <h5 class="abs" style="left:669px;top:88px">SERVICES</h5>
  <ul class="abs" style="left:669px;top:124px"><li>Watch Apps</li><li>Holographic Screens</li><li>Virtual Reality</li><li>Tablet &amp; Smartphone</li></ul>
  <div class="abs socials" style="left:962px;top:92px"><i style="border-color:#ccc;width:22px;height:22px"></i><i style="border-color:#ccc;width:22px;height:22px"></i><i style="border-color:#ccc;width:22px;height:22px"></i><i style="border-color:#ccc;width:22px;height:22px"></i></div>
  <div class="abs" style="left:126px;top:314px;width:947px;height:1px;background:#3a3a3a"></div>
  <div class="abs" style="left:0;top:354px;width:1200px;text-align:center;font-size:11.5px;color:#c8c8c8">© 2020 All Right Reserved. &nbsp;|&nbsp; Privacy Policy</div>
</footer>

</body>
</html>
```